Business Card Design needed for start up company Pramora

In need of a new business card designed for a start up company based in Sydney, Pramora is a new start up innovative Company, our mission it to make property accessible for everyday Australian and to become the leading Real Estate platform in Australia. We want it to be fresh and clean.

Industry/Entity Type

Financial

Contact Information for Business Card

Section for Name
Section for Title

PRAMORA - Where Doors Open Wide
Mobile:
Direct:

Font styles to use
Sans Serif

Colors
33a6d7
0692cd
0255a3
ffffff

Requirements
Must have
• Logo, all business card details

```html
<!DOCTYPE html>
<html lang="en">
<head>
<meta charset="UTF-8">
<title>Pramora Business Card</title>
<link rel="stylesheet" href="https://fonts.googleapis.com/css2?family=Roboto:wght@400;500&display=swap">
<style>
  :root {
    --navy: #1f4a7e;
    --ink: #4a4a4a;
    --white: #ffffff;
    --backdrop: #eef1f4;
    --rule: #3b7fb3;
  }
  * { margin: 0; padding: 0; box-sizing: border-box; }
  html, body {
    width: 1200px; height: 1200px; overflow: hidden;
    background: var(--backdrop);
    font-family: "Roboto", Arial, sans-serif;
  }
  .canvas { position: relative; width: 1200px; height: 1200px; }
  .card {
    position: absolute; left: 214px; width: 773px; height: 439px;
    border-radius: 18px;
    box-shadow: 0 6px 18px rgba(0,0,0,0.18);
  }
  .card-front { top: 151px; background: var(--white); }
  .card-back { top: 634px; background: var(--navy); }

  .brand-name {
    position: absolute; font-weight: 500; line-height: 1;
    letter-spacing: 2px; white-space: nowrap;
  }
  .card-front .brand-name {
    left: 40px; width: 320px; top: 196px; text-align: center;
    font-size: 46px; color: var(--navy);
  }

  .divider {
    position: absolute; left: 388px; top: 102px;
    width: 1.5px; height: 236px; background: var(--rule);
  }
  .details { position: absolute; left: 423px; top: 92px; color: var(--ink); }
  .person-name { font-size: 28px; font-weight: 500; color: var(--navy); line-height: 34px; }
  .person-title { font-size: 19.5px; line-height: 26px; }
  .address { font-size: 18px; line-height: 26px; margin-top: 24px; }
  .contact-list { list-style: none; margin-top: 16px; }
  .contact-list li {
    display: flex; align-items: center; gap: 8px;
    font-size: 18px; line-height: 27.5px;
  }
  .contact-list svg { width: 17px; height: 17px; flex: none; }

  .card-back .brand-name {
    left: 0; right: 0; top: 170px; text-align: center;
    font-size: 100px; color: var(--white);
  }
  .tagline {
    position: absolute; left: 0; right: 0; top: 382px;
    text-align: center; color: var(--white); font-size: 21px;
  }
</style>
</head>
<body>
<main class="canvas">
  <section class="card card-front">
    <span class="brand-name">PRAMORA</span>
    <div class="divider"></div>
    <div class="details">
      <h1 class="person-name">Daniel Hartley</h1>
      <p class="person-title">President &amp; CEO</p>
      <p class="address">220 Harbour Lane, Level 4<br>Sydney, NSW 2000</p>
      <ul class="contact-list">
        <li>
          <svg viewBox="0 0 24 24" fill="none" stroke="#4a4a4a" stroke-width="1.6" stroke-linejoin="round"><path d="M5 3h4l2 5-2.5 1.5a11 11 0 0 0 6 6L16 13l5 2v4a2 2 0 0 1-2 2A17 17 0 0 1 3 5a2 2 0 0 1 2-2z"/></svg>
          <span>000-000-0000</span>
        </li>
        <li>
          <svg viewBox="0 0 24 24" fill="none" stroke="#4a4a4a" stroke-width="1.6"><rect x="6" y="2" width="12" height="20" rx="2"/><line x1="11" y1="18" x2="13" y2="18"/></svg>
          <span>000-000-0000</span>
        </li>
        <li>
          <svg viewBox="0 0 24 24" fill="none" stroke="#4a4a4a" stroke-width="1.6"><rect x="3" y="5" width="18" height="14"/><path d="M3 5l9 8 9-8"/></svg>
          <span>d.hartley@pramora-homes.com</span>
        </li>
        <li>
          <svg viewBox="0 0 24 24" fill="none" stroke="#4a4a4a" stroke-width="1.6"><circle cx="12" cy="12" r="9"/><ellipse cx="12" cy="12" rx="4" ry="9"/><line x1="3" y1="12" x2="21" y2="12"/></svg>
          <span>www.pramora-homes.com</span>
        </li>
      </ul>
    </div>
  </section>

  <section class="card card-back">
    <span class="brand-name">PRAMORA</span>
    <p class="tagline">Where Doors Open Wide</p>
  </section>
</main>
</body>
</html>
```